Packaging design for a Deli Shop "TERU Gourmet"

We need a packaging design for a new Deli Business we are opening soon. We produce food to be packaged and sold either fresh or frozen in transparent disposable plastic boxes, cardboard boxes and finally delivered in a bag (Paper, plastic or shopping bag whatever goes best with the design) to take out. The food we generally pack are salads, lasagnas, ceviches, sandwiches, cookies, granola, dips, etc.

The name of the company is "TERU Gourmet" Check our website for reference: www.terugourmet-example.com

We have a logo and a name we want to maintain (attached).

The product will be sold in our new deli store, that is inspired in big cities delikatessen, quite modern and trendy. It also delivers a message that everything we sell is high quality, artisan (not massive or mainstream) and great in flavors.

Packaging must communicate freshness, great flavor, high quality and high price.

Packaging must be feasible to produce and print easily without any complex or impossible to implement packaging, (preferrable to be done or easy to adapt from generic packaging).

All our communication will be in Spanish so please do not depend on english for the design. If english or any other language is used, please be sure its understandable in almost any country (ie Basic English, Italian).

Same packaging (labeling or boxes and bags) will be used, just changing the name of the product inside according to the product.

Most of our product will be displayed in refrigerators and freezers.
Updates

I just uploaded a visual brief of the packaging examples we would like to have.

Looking forward to see your designs.
Thank you

Reason: Some designers who said will participate havent submitted their deaigns, and still what is being submitted is not fully complying with the requirements. Thank you

Target Market(s)

The main target is High SEL, between 24 and 40, mostly woman

Industry/Entity Type

Communication

Requirements
Must have

Nice to have
• Please take a look at my website www.terugourmet-example.com to see the kind of coloring we are aiming to have.

Give the impression of being "Green"...

Include "Kraft" color paper / Brown paper color
Should not have
• Complex packaging difficult to implement in a simple print shop.
Expensive items.

```html
<!DOCTYPE html>
<html lang="en">
<head>
<meta charset="utf-8">
<title>TERU Gourmet — Packaging Range</title>
<link rel="stylesheet" href="https://fonts.googleapis.com/css2?family=Quicksand:wght@500;600&display=swap">
<style>
  :root {
    --brown: #2f2118;
    --kraft: #c9a06a;
    --kraft-light: #d8b683;
    --green: #8dc63f;
    --orange: #f2a23a;
    --red: #f15a29;
    --white: #ffffff;
    --paper: #f4f4f4;
    --text-font: "Quicksand", sans-serif;
  }
  * { box-sizing: border-box; margin: 0; padding: 0; }
  html, body { width: 1200px; height: 848px; overflow: hidden; background: var(--white); }
  .canvas { position: relative; width: 1200px; height: 848px; font-family: var(--text-font); }
  .piece, .piece * { position: absolute; }

  /* shared elements */
  .brand-mark {
    display: flex; align-items: center; justify-content: center; gap: 0.35em;
    font-weight: 600; line-height: 1; white-space: nowrap;
  }
  .brand-mark .brand-dot, .brand-mark .brand-name { position: static; }
  .brand-mark .brand-dot { width: 0.6em; height: 0.6em; background: var(--green); }
  .brand-mark.on-kraft { color: var(--brown); }
  .brand-mark.on-dark { color: var(--white); }
  .kraft { background: var(--kraft); }
  .dark { background: var(--brown); }
  .fresh-strip { background: var(--green); }
  .tile-band {
    background: linear-gradient(90deg, var(--green), var(--orange) 35%, var(--red) 65%, var(--orange) 85%, var(--green));
    opacity: 0.9;
  }
  .product-title { color: var(--white); font-weight: 500; line-height: 1.12; }
  .product-note { color: var(--green); font-weight: 500; }

  /* cookie pouch */
  .cookie-pouch { left: 92px; top: 63px; width: 243px; height: 349px; background: var(--brown); }
  .cookie-pouch .brand-mark { left: 0; top: 52px; width: 243px; font-size: 17px; }
  .cookie-pouch .kraft { left: 0; top: 101px; width: 243px; height: 94px; }
  .cookie-pouch .fresh-strip { left: 0; top: 94px; width: 243px; height: 7px; }
  .cookie-pouch .cookie-photo { top: 121px; width: 52px; height: 52px; border-radius: 50%;
    background: radial-gradient(circle, #b57b45, #8a5429); }
  .cookie-pouch .cookie-left { left: 14px; }
  .cookie-pouch .cookie-right { left: 176px; }
  .cookie-pouch .product-title { left: 0; top: 135px; width: 243px; text-align: center; color: var(--brown); font-size: 17px; }
  .cookie-pouch .tile-band { left: 4px; top: 222px; width: 235px; height: 56px; }
  .cookie-pouch .net-weight { left: 0; top: 309px; width: 243px; text-align: center; color: var(--white); font-size: 9px; font-weight: 600; letter-spacing: 0.03em; }

  /* jar label */
  .jar-label { left: 451px; top: 117px; width: 91px; height: 141px; background: var(--brown); }
  .jar-label .kraft { left: 0; top: 0; width: 91px; height: 72px; }
  .jar-label .brand-mark { left: 0; top: 30px; width: 91px; font-size: 11px; }
  .jar-label .tile-band { left: 2px; top: 90px; width: 87px; height: 40px; }

  /* sandwich box */
  .sandwich-panel { left: 666px; top: 94px; width: 125px; height: 286px; background: var(--brown); }
  .sandwich-panel .kraft { left: 0; top: 0; width: 125px; height: 103px; }
  .sandwich-panel .brand-mark { left: 0; top: 44px; width: 125px; font-size: 14px; }
  .sandwich-panel .fresh-strip { left: 0; top: 103px; width: 125px; height: 7px; }
  .sandwich-panel .window { left: 17px; top: 126px; width: 91px; height: 140px; background: var(--white); border-radius: 4px; }
  .sandwich-panel .window .tile-band { left: 2px; top: 104px; width: 87px; height: 32px; }
  .sandwich-wedge { left: 818px; top: 94px; width: 283px; height: 286px; }
  .sandwich-wedge svg { left: 0; top: 0; }
  .sandwich-wedge .tile-band { left: 0; top: 109px; width: 112px; height: 55px; }
  .sandwich-wedge .product-title { left: 17px; top: 188px; font-size: 17px; }
  .sandwich-wedge .product-note { left: 17px; top: 233px; width: 200px; font-size: 9.5px; line-height: 1.35; }

  /* salad tray sleeve */
  .salad-sleeve { left: 162px; top: 513px; width: 111px; height: 239px; background: var(--brown); }
  .salad-sleeve .kraft { left: 0; top: 0; width: 111px; height: 100px; }
  .salad-sleeve .brand-mark { left: 0; top: 44px; width: 111px; font-size: 13px; }
  .salad-sleeve .fresh-strip { left: 0; top: 100px; width: 111px; height: 8px; }
  .salad-sleeve .product-title { left: 9px; top: 117px; font-size: 18px; }
  .salad-sleeve .product-note { left: 9px; top: 160px; font-size: 10px; }
  .salad-sleeve .tile-band { left: 4px; top: 187px; width: 103px; height: 52px; }

  /* granola wrapper */
  .granola-wrap { left: 525px; top: 570px; width: 280px; height: 105px; background: var(--paper); }
  .granola-wrap .brand-mark { left: 0; top: 47px; width: 101px; font-size: 10px; }
  .granola-wrap .dark { left: 101px; top: 14px; width: 139px; height: 80px; }
  .granola-wrap .product-title { left: 13px; top: 9px; font-size: 11px; }
  .granola-wrap .product-note { left: 13px; top: 24px; font-size: 8.5px; }
  .granola-wrap .tile-band { left: 12px; top: 40px; width: 92px; height: 36px; }

  /* take-out bag */
  .takeout-bag { left: 862px; top: 515px; width: 240px; height: 263px; background: var(--kraft-light); }
  .takeout-bag .brand-mark { left: 0; top: 60px; width: 240px; font-size: 18px; }
  .takeout-bag .dark { left: 0; top: 104px; width: 240px; height: 99px; }
  .takeout-bag .tile-band { left: 0; top: 139px; width: 240px; height: 58px; }
</style>
</head>
<body>
<main class="canvas">

  <section class="piece cookie-pouch" aria-label="Cookie pouch">
    <div class="brand-mark on-dark"><span class="brand-dot"></span><span class="brand-name">TERU Gourmet</span></div>
    <div class="fresh-strip"></div>
    <div class="kraft"></div>
    <div class="cookie-photo cookie-left" role="img" aria-label="Photo of chocolate chip cookies"></div>
    <div class="cookie-photo cookie-right" role="img" aria-label="Photo of chocolate chip cookies"></div>
    <p class="product-title">Chocolate<br>Cookies</p>
    <div class="tile-band" role="img" aria-label="Zigzag band of green, orange and red squares"></div>
    <p class="net-weight">NETT WT 250 gr</p>
  </section>

  <section class="piece jar-label" aria-label="Jar label">
    <div class="kraft"></div>
    <div class="brand-mark on-kraft"><span class="brand-dot"></span><span class="brand-name">TERU Gourmet</span></div>
    <div class="tile-band" role="img" aria-label="Zigzag band of green, orange and red squares"></div>
  </section>

  <section class="piece sandwich-panel" aria-label="Sandwich box side panel">
    <div class="kraft"></div>
    <div class="brand-mark on-kraft"><span class="brand-dot"></span><span class="brand-name">TERU Gourmet</span></div>
    <div class="fresh-strip"></div>
    <div class="window">
      <div class="tile-band" role="img" aria-label="Zigzag band of green, orange and red squares"></div>
    </div>
  </section>

  <section class="piece sandwich-wedge" aria-label="Sandwich box front">
    <svg width="283" height="286" viewBox="0 0 283 286"><polygon points="0,0 0,286 283,286" fill="var(--brown)"/></svg>
    <div class="tile-band" role="img" aria-label="Zigzag band of green, orange and red squares"></div>
    <p class="product-title">Tuna<br>Egg Mayo</p>
    <p class="product-note">can tuna, hard-cooked eggs, celery,<br>mayonnaise, salt and pepper,<br>whole wheat bread</p>
  </section>

  <section class="piece salad-sleeve" aria-label="Salad tray sleeve">
    <div class="kraft"></div>
    <div class="brand-mark on-kraft"><span class="brand-dot"></span><span class="brand-name">TERU Gourmet</span></div>
    <div class="fresh-strip"></div>
    <p class="product-title">Fresh<br>Salad</p>
    <p class="product-note">chicken caesar</p>
    <div class="tile-band" role="img" aria-label="Zigzag band of green, orange and red squares"></div>
  </section>

  <section class="piece granola-wrap" aria-label="Granola bar wrapper">
    <div class="brand-mark on-kraft"><span class="brand-dot"></span><span class="brand-name">TERU Gourmet</span></div>
    <div class="dark">
      <p class="product-title">Granola Bar</p>
      <p class="product-note">oats &amp; honey</p>
      <div class="tile-band" role="img" aria-label="Zigzag band of green, orange and red squares"></div>
    </div>
  </section>

  <section class="piece takeout-bag" aria-label="Take-out paper bag front">
    <div class="brand-mark on-kraft"><span class="brand-dot"></span><span class="brand-name">TERU Gourmet</span></div>
    <div class="dark"></div>
    <div class="tile-band" role="img" aria-label="Zigzag band of green, orange and red squares"></div>
  </section>

</main>
</body>
</html>
```